Business Card for Quillmark Ledger - A cannabis publication for executives.

I'd like some business cards for Quillmark Ledger. The logo is done (great job!) and I need a card design I will use with PRINTLY. I made it a short project to allow time for printing before an event. These will be standard sized cards (final artwork size 3.66" x 2.16" at 300dpi) with a final card size of 3.5" x 2.0". (See PRINTLY.com if you need more info.) I might try rounded corners but am not sure yet. I think the design will work okay with rounded.

Quillmark Ledger will be a bi-weekly publication for the cannabis industry. It is targeted to investors and industry executives, not consumers or pot smokers. So our market is more B2B. However I am open to creativity and making the card something people remark on.

My contact for card:

Dana Merrow
Founder/CEO
dana@quillmarkledger.example

2740 Harlow Avenue
Boston MA 02135
(617)555-0194

Target Market(s)

Executives, Industry people and investors in the Cannabis sector.

Contact Information for Business Card

PRINTLY does do double sided and the second side can be the same or different images. Only one side is required but use of the second side would be a bonus.

Font styles to use
Serif
Sans Serif
Decorative

Colors

Designer to choose colors to be used in the design.

Requirements
Must have
• Logo, contact info
Nice to have
• Style and design to make the card stand out in a crowd.

```html
<!DOCTYPE html>
<html lang="en">
<head>
<meta charset="utf-8">
<title>Quillmark Ledger — Business Card</title>
<link href="https://fonts.googleapis.com/css2?family=Gelasio:wght@400;700&display=swap" rel="stylesheet">
<style>
  :root {
    --backdrop: #e3e3e3;
    --card-white: #ffffff;
    --leaf-green: #82ad35;
    --ledger-blue: #0a75bc;
    --ink: #222222;
  }
  * { margin: 0; padding: 0; box-sizing: border-box; }
  html, body {
    width: 1200px; height: 960px; overflow: hidden;
    background: var(--backdrop);
    font-family: "Gelasio", Georgia, serif;
  }
  .stage {
    width: 1200px; height: 960px;
    display: flex; align-items: center; justify-content: center; gap: 40px;
  }
  .card {
    width: 540px; height: 309px;
    border-radius: 26px;
    position: relative;
    overflow: hidden;
    box-shadow: 0 4px 14px rgba(0,0,0,0.12);
  }
  .card--front { background: var(--card-white); }
  .card--back {
    background: var(--leaf-green);
    display: flex; align-items: center; justify-content: center; gap: 16px;
  }

  /* front */
  .brand-block {
    position: absolute; left: 34px; top: 44px; width: 210px;
    display: flex; flex-direction: column; align-items: flex-start; gap: 14px;
  }
  .brand-square {
    width: 96px; height: 96px; background: var(--leaf-green);
  }
  .brand-name {
    color: var(--ledger-blue); font-size: 30px; line-height: 1.1; font-weight: 700;
  }
  .contact {
    position: absolute; left: 252px; top: 58px; right: 0;
  }
  .contact__name {
    color: var(--ledger-blue); font-weight: 700; font-size: 25px;
    letter-spacing: 0.5px; text-transform: uppercase; line-height: 1.1;
  }
  .contact__title {
    color: var(--leaf-green); font-size: 19px; margin-top: 4px;
  }
  .contact__address {
    color: var(--ink); font-size: 13.5px; margin-top: 14px;
  }
  .contact__phone-band {
    margin-top: 8px; background: var(--ledger-blue); color: var(--card-white);
    font-size: 24px; padding: 6px 14px; height: 44px; line-height: 32px;
  }
  .contact__email {
    color: var(--ink); font-size: 13.5px; margin-top: 10px;
  }

  /* back */
  .back-square { width: 58px; height: 58px; background: var(--card-white); }
  .back-name { color: var(--card-white); font-size: 40px; font-weight: 400; }
</style>
</head>
<body>
  <main class="stage">
    <section class="card card--front" aria-label="Card front">
      <div class="brand-block">
        <div class="brand-square"></div>
        <div class="brand-name">Quillmark Ledger</div>
      </div>
      <div class="contact">
        <h1 class="contact__name">Dana Merrow</h1>
        <p class="contact__title">Founder/CEO</p>
        <p class="contact__address">2740 Harlow Avenue Boston MA 02135</p>
        <p class="contact__phone-band">(617) 555 0194</p>
        <p class="contact__email">dana@quillmarkledger.example</p>
      </div>
    </section>
    <section class="card card--back" aria-label="Card back">
      <div class="back-square"></div>
      <div class="back-name">Quillmark Ledger</div>
    </section>
  </main>
</body>
</html>
```